Design for Outdoor Events Postcard

I need a postcard design 2 sided for outdoor workshop events that are targeted at individuals and business teams. The concept of the outdoor workshops is closely related to nature, grounding oneself with nature, mindfulness, making conscious decisions, improving communication, growing as a team by accepting each others differences and more. Hence, the background/basic design concept of the postcard needs to related to nature. Also, using both logos, The Open Meadow and the company logo is important. The final design needs to be warm, inviting, creating interest for wanting to learn more, elegant (retro is ok too). Do not use cliché like photos of business people or corporate designs. If you want to use photos of nature, you can use the attached or your own. Please check our website www.brightcoveadvisory.com/events for more information. You can use the attached postcard for context. Also the website offers a lot for context. The postcard size is US standard 6x4.25 inches.

Industry/Entity Type

Events

Requirements
Should not have
• I have attached 5 postcard designs that don't work for me at all for different reasons. If you need more details, please get in touch with me.

```html
<!DOCTYPE html>
<html lang="en">
<head>
<meta charset="utf-8">
<title>Bright Cove Advisory – Outdoor Events Postcard</title>
<link href="https://fonts.googleapis.com/css2?family=Open+Sans:ital,wght@0,400;0,600;0,700;1,400&display=swap" rel="stylesheet">
<style>
  :root {
    --page-bg: #e6e6e6;
    --card-white: #ffffff;
    --leaf-green: #8cc63f;
    --brand-blue: #2e9bd6;
    --text-grey: #6d6d6d;
    --text-dark: #333333;
    --sky-top: #7fb5e8;
    --sky-low: #c9dff2;
    --foliage: #3f6b2a;
    --foliage-dark: #27461b;
  }
  * { margin: 0; padding: 0; box-sizing: border-box; }
  html, body { width: 1200px; height: 1000px; overflow: hidden; }
  body {
    background: var(--page-bg);
    font-family: "Open Sans", Arial, sans-serif;
    position: relative;
  }
  .postcard {
    position: absolute;
    left: 100px; top: 146px;
    width: 1000px; height: 708px;
    background: var(--card-white);
    box-shadow: 0 6px 24px rgba(0,0,0,0.18);
    overflow: hidden;
  }
  .postcard-art { position: absolute; inset: 0; }
  .contact-list {
    position: absolute; left: 34px; top: 26px;
    list-style: none;
  }
  .contact-item {
    display: flex; align-items: center; gap: 14px;
    color: var(--leaf-green); font-size: 15px; font-weight: 600;
    height: 30px;
  }
  .contact-icon { width: 22px; height: 22px; }
  .brand {
    position: absolute; right: 40px; top: 38px;
    display: flex; align-items: center; gap: 12px;
  }
  .brand-dot {
    width: 22px; height: 22px; border-radius: 50%;
    background: var(--leaf-green);
  }
  .brand-name {
    color: var(--brand-blue); font-size: 34px; font-weight: 700;
    letter-spacing: -0.5px;
  }
  .intro-panel {
    position: absolute; left: 440px; top: 356px;
    width: 545px; height: 122px;
    background: rgba(255,255,255,0.62);
    border-radius: 16px;
    padding: 14px 18px;
    text-align: right;
    font-style: italic; font-size: 15.5px; line-height: 1.42;
    color: var(--text-dark);
  }
  .invite {
    position: absolute; left: 58px; top: 515px;
    color: var(--text-grey);
    font-style: italic; font-size: 27px; line-height: 1.25;
  }
  .invite-note {
    position: absolute; left: 42px; top: 594px; width: 330px;
    color: var(--text-dark);
    font-weight: 700; font-size: 16px; line-height: 1.3;
  }
</style>
</head>
<body>
  <article class="postcard">
    <svg class="postcard-art" viewBox="0 0 1000 708" width="1000" height="708">
      <defs>
        <linearGradient id="scene-tone" x1="0" y1="0" x2="0" y2="1">
          <stop offset="0" stop-color="var(--sky-top)"/>
          <stop offset="0.42" stop-color="var(--sky-low)"/>
          <stop offset="0.55" stop-color="var(--foliage)"/>
          <stop offset="1" stop-color="var(--foliage-dark)"/>
        </linearGradient>
      </defs>
      <path role="img" aria-label="Photo of a coastal nature trail with trees, shrubs and the ocean under a blue sky"
            d="M0 112 C 300 92, 650 110, 1000 172 L 1000 598 C 700 560, 350 460, 0 468 Z"
            fill="url(#scene-tone)"/>
      <path class="swoosh-top" d="M0 112 C 300 92, 650 110, 1000 172"
            fill="none" stroke="var(--leaf-green)" stroke-width="12"/>
      <path class="swoosh-bottom" d="M0 468 C 350 460, 700 560, 1000 598"
            fill="none" stroke="var(--leaf-green)" stroke-width="12"/>
    </svg>

    <ul class="contact-list">
      <li class="contact-item">
        <svg class="contact-icon" viewBox="0 0 22 22" aria-hidden="true">
          <circle cx="11" cy="11" r="10" fill="var(--brand-blue)"/>
          <path d="M1 11h20M11 1c-4 5-4 15 0 20M11 1c4 5 4 15 0 20" fill="none" stroke="#fff" stroke-width="1.3"/>
        </svg>
        www.brightcoveadvisory.com/events
      </li>
      <li class="contact-item">
        <svg class="contact-icon" viewBox="0 0 22 22" aria-hidden="true">
          <rect x="6" y="1" width="11" height="20" rx="2.5" fill="none" stroke="var(--brand-blue)" stroke-width="2"/>
          <circle cx="11.5" cy="17" r="1.3" fill="var(--brand-blue)"/>
        </svg>
        555.014.2290
      </li>
    </ul>

    <div class="brand">
      <span class="brand-dot"></span>
      <span class="brand-name">Bright Cove Advisory</span>
    </div>

    <p class="intro-panel">Bright Cove Advisory invites you to explore how the 'noise' in your work and life impacts overall wellbeing and performance. Through connection with nature, we'll explore new ways of being in service of yourself and others resulting in more fulfillment and success.</p>

    <p class="invite">You don't want to miss this powerful<br>one-day “RootedTogether” experience!</p>
    <p class="invite-note">See reverse for upcoming dates and locations!</p>
  </article>
</body>
</html>
```